Business cards

I would like a black background with the design I previously chose. I need 2 sets of cards. Mine will have Marisol Brandt, Broker/Owner, 307-555-0148 and marisol.harborpeak@mailvista.com
The second set will read, Dana Rutledge, Realtor 307-555-0172, dana.harborpeak@mailvista.com

Industry/Entity Type

Business

```html
<!DOCTYPE html>
<html lang="en">
<head>
<meta charset="utf-8">
<title>Harbor Peak Business Cards</title>
<link href="https://fonts.googleapis.com/css2?family=Marcellus&family=Lato:wght@400&display=swap" rel="stylesheet">
<style>
  :root {
    --page: #ffffff;
    --card: #0b0b0b;
    --card-edge: #161616;
    --facet-light: #232323;
    --ink: #e8e6e1;
    --ink-soft: #c9c6bf;
    --mark: #bdb9ae;
    --rule: #8c8a84;
    --rig: #2b2b2b;
  }
  * { margin: 0; padding: 0; box-sizing: border-box; }
  html, body { width: 1200px; height: 1200px; overflow: hidden; background: var(--page); }
  .sheet { position: relative; width: 1200px; height: 1200px; }
  .card {
    position: absolute; top: 480px; width: 403px; height: 238px;
    background: radial-gradient(ellipse at 30% 20%, var(--card-edge), var(--card) 70%);
    overflow: hidden;
  }
  .card--broker { left: 180px; }
  .card--realtor { left: 616px; }
  .card__texture {
    position: absolute; inset: 0;
    background: linear-gradient(125deg, transparent 0%, rgba(255,255,255,0.03) 30%, transparent 55%, rgba(255,255,255,0.025) 80%, transparent 100%);
  }
  .card__rig {
    position: absolute; left: 252px; top: 64px; width: 128px; height: 150px;
    background: linear-gradient(180deg, rgba(60,60,60,0.35), rgba(40,40,40,0.55));
    border-radius: 2px;
  }
  .brand { position: absolute; left: 20px; top: 22px; width: 100px; text-align: center; }
  .brand__dot {
    display: block; width: 40px; height: 40px; margin: 0 auto 3px;
    border-radius: 50%; background: var(--mark);
  }
  .brand__name {
    font-family: "Marcellus", serif; font-size: 11.5px; color: var(--mark);
    letter-spacing: 0.2px; white-space: nowrap; line-height: 1.1;
  }
  .brand__sub {
    font-family: "Marcellus", serif; font-size: 4.6px; color: var(--mark);
    letter-spacing: 1.4px; text-transform: uppercase; line-height: 1.2;
    border-top: 1px solid var(--rule); margin-top: 1px; padding-top: 1px;
  }
  .person { position: absolute; left: 160px; top: 65px; width: 180px; text-align: center; }
  .person__name {
    font-family: "Marcellus", serif; font-size: 14px; color: var(--ink);
    text-transform: uppercase; letter-spacing: 0.6px; line-height: 1.1;
  }
  .person__role {
    font-family: "Marcellus", serif; font-size: 8.5px; color: var(--ink-soft);
    letter-spacing: 1.6px; margin-top: 3px;
  }
  .contact { position: absolute; left: 22px; top: 178px; list-style: none; }
  .contact__item {
    display: flex; align-items: center; gap: 7px; height: 13px;
    font-family: "Lato", sans-serif; font-size: 9.5px; color: var(--ink-soft);
  }
  .contact__icon { width: 10px; height: 10px; flex: none; }
</style>
</head>
<body>
<div class="sheet">

  <article class="card card--broker">
    <div class="card__texture" role="img" aria-label="Faint faceted dark polygon background pattern"></div>
    <div class="card__rig" role="img" aria-label="Faint silhouette of an oil pumpjack"></div>
    <div class="brand">
      <span class="brand__dot"></span>
      <div class="brand__name">HARBOR PEAK</div>
      <div class="brand__sub">Real Estate Group LLC</div>
    </div>
    <div class="person">
      <div class="person__name">Marisol Brandt</div>
      <div class="person__role">Broker/Owner</div>
    </div>
    <ul class="contact">
      <li class="contact__item">
        <svg class="contact__icon" viewBox="0 0 10 10"><rect x="0" y="0" width="10" height="10" rx="2.5" fill="#cfccc5"/><rect x="3" y="2" width="4" height="6" rx="0.8" fill="none" stroke="#0b0b0b" stroke-width="1"/></svg>
        307-555-0148
      </li>
      <li class="contact__item">
        <svg class="contact__icon" viewBox="0 0 10 10"><circle cx="5" cy="5" r="5" fill="#cfccc5"/><circle cx="5" cy="5" r="2.8" fill="none" stroke="#0b0b0b" stroke-width="0.9"/><path d="M2.2 5h5.6M5 2.2v5.6" stroke="#0b0b0b" stroke-width="0.8"/></svg>
        marisol.harborpeak@mailvista.com
      </li>
    </ul>
  </article>

  <article class="card card--realtor">
    <div class="card__texture" role="img" aria-label="Faint faceted dark polygon background pattern"></div>
    <div class="card__rig" role="img" aria-label="Faint silhouette of an oil pumpjack"></div>
    <div class="brand">
      <span class="brand__dot"></span>
      <div class="brand__name">HARBOR PEAK</div>
      <div class="brand__sub">Real Estate Group LLC</div>
    </div>
    <div class="person">
      <div class="person__name">Dana Rutledge</div>
      <div class="person__role">Realtor</div>
    </div>
    <ul class="contact">
      <li class="contact__item">
        <svg class="contact__icon" viewBox="0 0 10 10"><rect x="0" y="0" width="10" height="10" rx="2.5" fill="#cfccc5"/><rect x="3" y="2" width="4" height="6" rx="0.8" fill="none" stroke="#0b0b0b" stroke-width="1"/></svg>
        307-555-0172,
      </li>
      <li class="contact__item">
        <svg class="contact__icon" viewBox="0 0 10 10"><circle cx="5" cy="5" r="5" fill="#cfccc5"/><circle cx="5" cy="5" r="2.8" fill="none" stroke="#0b0b0b" stroke-width="0.9"/><path d="M2.2 5h5.6M5 2.2v5.6" stroke="#0b0b0b" stroke-width="0.8"/></svg>
        dana.harborpeak@mailvista.com
      </li>
    </ul>
  </article>

</div>
</body>
</html>
```